Modern Design Business Card industrial maintenance company

Business card design for Company named Brookvale Equipment Services

Target Market(s)

Industrial

Industry/Entity Type

Maintenance and repair

Contact Information for Business Card

Place holder for address, office phone, mobile number and email

Requirements
Must have
• Clean modern look
Nice to have
• N/a

```html
<!DOCTYPE html>
<html lang="en">
<head>
<meta charset="utf-8">
<title>Brookvale Equipment Services – Business Card</title>
<link rel="stylesheet" href="https://fonts.googleapis.com/css2?family=Roboto:wght@300;400;500;700&display=swap">
<style>
  :root {
    --backdrop: #d9d9dc;
    --card-dark: #1f1f26;
    --card-light: #ffffff;
    --ink: #111114;
    --ink-soft: #3a3a3f;
    --silver: #d8d8dc;
    --rule: #4a4a4f;
  }
  * { box-sizing: border-box; margin: 0; padding: 0; }
  html, body {
    width: 1200px; height: 800px; overflow: hidden;
    background: var(--backdrop);
    font-family: "Roboto", Arial, sans-serif;
  }
  .canvas {
    position: relative; width: 1200px; height: 800px;
    display: flex; align-items: center; justify-content: center; gap: 50px;
  }
  .card {
    position: relative; width: 525px; height: 300px;
    border-radius: 18px; overflow: hidden;
    box-shadow: 0 14px 30px rgba(0,0,0,.25);
  }

  /* Front */
  .card--front { background: var(--card-dark); }
  .front-brand {
    position: absolute; inset: 0;
    display: flex; align-items: center; justify-content: center; gap: 18px;
  }
  .brand-circle {
    width: 70px; height: 70px; border-radius: 50%;
    border: 2.5px solid var(--silver); flex: none;
  }
  .front-brand .brand-name {
    color: var(--silver); font-weight: 400; font-size: 25px;
    letter-spacing: 3px; text-transform: uppercase; line-height: 1.25;
  }

  /* Back */
  .card--back { background: var(--card-light); color: var(--ink); }
  .back-brand {
    position: absolute; top: 24px; right: 36px;
    display: flex; align-items: center; gap: 14px;
  }
  .back-brand .brand-circle { width: 54px; height: 54px; border-color: var(--ink); border-width: 3px; }
  .back-brand .brand-name {
    font-weight: 500; font-size: 16px; letter-spacing: 2px;
    text-transform: uppercase; line-height: 1.3; color: var(--ink);
  }
  .person {
    position: absolute; top: 96px; left: 34px; right: 36px;
    display: flex; align-items: center; gap: 12px;
  }
  .person-name { font-size: 20px; font-weight: 700; letter-spacing: .5px; text-transform: uppercase; white-space: nowrap; }
  .person-rule { flex: 1; height: 1px; background: var(--rule); }
  .person-title {
    position: absolute; left: 34px; top: 128px;
    font-size: 14px; font-weight: 300; color: var(--ink-soft);
  }
  .address {
    position: absolute; top: 132px; right: 36px; text-align: right;
    font-size: 14.5px; font-weight: 300; line-height: 1.4; color: var(--ink-soft);
    font-style: normal;
  }
  .contacts {
    position: absolute; left: 34px; bottom: 22px; list-style: none;
    font-size: 14.5px; font-weight: 300; line-height: 1.45; color: var(--ink-soft);
  }
  .contacts li { display: flex; align-items: center; gap: 9px; }
  .contacts svg { width: 13px; height: 13px; flex: none; }
  .edge-tab {
    position: absolute; left: 0; bottom: 56px; width: 12px; height: 28px; background: var(--ink);
  }
</style>
</head>
<body>
<main class="canvas">
  <section class="card card--front" aria-label="Card front">
    <div class="front-brand">
      <span class="brand-circle" aria-hidden="true"></span>
      <span class="brand-name">Brookvale<br>Equipment Services</span>
    </div>
  </section>

  <section class="card card--back" aria-label="Card back">
    <div class="back-brand">
      <span class="brand-circle" aria-hidden="true"></span>
      <span class="brand-name">Brookvale<br>Equipment Services</span>
    </div>

    <div class="person">
      <span class="person-name">Daniel Marsh</span>
      <span class="person-rule"></span>
    </div>
    <div class="person-title">Managing Director</div>

    <address class="address">
      Brookvale Equipment Services<br>
      118 W Harlan St<br>
      Ridgeford, CA 93012
    </address>

    <ul class="contacts">
      <li>
        <svg viewBox="0 0 16 16" aria-hidden="true"><rect x="4" y="1" width="8" height="14" rx="1.5" fill="none" stroke="#111114" stroke-width="1.6"/><rect x="7" y="12" width="2" height="1.2" fill="#111114"/></svg>
        (555) 204-7316
      </li>
      <li>
        <svg viewBox="0 0 16 16" aria-hidden="true"><rect x="1" y="3" width="14" height="10" rx="1" fill="#111114"/><path d="M1.5 3.8 8 9l6.5-5.2" fill="none" stroke="#fff" stroke-width="1.2"/></svg>
        info@brookvaleequip.com
      </li>
      <li>
        <svg viewBox="0 0 16 16" aria-hidden="true"><circle cx="8" cy="8" r="7" fill="#111114"/><path d="M1 8h14M8 1c-3 3.5-3 10.5 0 14M8 1c3 3.5 3 10.5 0 14" fill="none" stroke="#fff" stroke-width=".9"/></svg>
        www.brookvaleequip.com
      </li>
    </ul>
    <span class="edge-tab" aria-hidden="true"></span>
  </section>
</main>
</body>
</html>
```